Hearth And Loom Biz Card Design

That example is too complicated. Hearth And Loom is my home design business.

I design Interiors, Exteriors and Home Staging.

My tag line is: BRINGING BRIGHT IDEAS TO INTERIORS, EXTERIORS AND HOME STAGING.

I would like a clean, simple, modern (sort of Helvetica-ish) design that includes an image of a light bulb. The bulb and the text should blend seamlessly.

I prefer a white background; black text; and blue highlights (lightbulb); not a greenish blue, not a navy blue. A color that mixes the best of both. Green/Blue. Not turquoise.

The color scheme should be elegant. And modern. Professional. Not quite 'too hip for the room'.

Sorta ignore the logo design example that is attached.

Let me know any questions! Look forward, thank you Carla

Business

Carla M Vandrell
Senior Design Specialist
Tel: 310-574-2936
Web: carla@hearthandloomhome.com

• Font and color

```html
<!DOCTYPE html>
<html lang="en">
<head>
<meta charset="utf-8">
<title>Hearth And Loom — Business Card</title>
<link href="https://fonts.googleapis.com/css2?family=Questrial&display=swap" rel="stylesheet">
<style>
  :root {
    --page: #ffffff;
    --card: #ffffff;
    --card-edge: #d6d9db;
    --ink: #111111;
    --teal: #1d7b8f;
    --teal-line: #2a8ea2;
    --teal-soft: #d8ecf0;
    --on-teal: #ffffff;
  }
  * { box-sizing: border-box; margin: 0; padding: 0; }
  html, body {
    width: 1200px;
    height: 700px;
    overflow: hidden;
    background: var(--page);
    font-family: "Questrial", "Helvetica Neue", Arial, sans-serif;
  }
  .card {
    position: absolute;
    left: 10px;
    top: 10px;
    width: 1180px;
    height: 680px;
    border-radius: 40px;
    background: var(--card);
    border: 2px solid var(--card-edge);
    box-shadow: 0 4px 10px rgba(0,0,0,0.12);
    overflow: hidden;
  }
  .brand-dot {
    position: absolute;
    left: 520px;
    top: 50px;
    width: 140px;
    height: 140px;
    border-radius: 50%;
    background: var(--teal-soft);
    border: 6px solid var(--teal);
  }
  .brand-name {
    position: absolute;
    left: 490px;
    top: 210px;
    font-size: 48px;
    line-height: 56px;
    color: var(--teal);
    letter-spacing: 0.5px;
    white-space: nowrap;
  }
  .tagline {
    position: absolute;
    left: 40px;
    top: 330px;
    font-size: 32px;
    line-height: 42px;
    color: var(--ink);
    letter-spacing: 0.3px;
  }
  .divider {
    position: absolute;
    left: 0;
    top: 510px;
    width: 100%;
    height: 6px;
    background: var(--teal-line);
  }
  .contact-band {
    position: absolute;
    left: 0;
    top: 526px;
    width: 100%;
    height: 160px;
    background: var(--teal);
    color: var(--on-teal);
  }
  .person {
    position: absolute;
    left: 245px;
    top: 30px;
    white-space: nowrap;
  }
  .person-name {
    font-size: 40px;
    letter-spacing: 0.5px;
  }
  .person-title {
    font-size: 27px;
    margin-left: 12px;
  }
  .details {
    position: absolute;
    left: 245px;
    top: 90px;
    font-size: 28px;
    letter-spacing: 1px;
    white-space: nowrap;
  }
  .details .email { margin-left: 90px; }
</style>
</head>
<body>
  <main class="card">
    <div class="brand-dot"></div>
    <div class="brand-name">Hearth And Loom</div>

    <p class="tagline">Bringing Bright Ideas to Interiors,<br>Exteriors and Home Staging.</p>

    <div class="divider"></div>

    <section class="contact-band">
      <div class="person">
        <span class="person-name">Carla M Vandrell</span>
        <span class="person-title">Senior Design Specialist</span>
      </div>
      <div class="details">
        <span class="phone">310-574-2936</span>
        <span class="email">carla@hearthandloomhome.com</span>
      </div>
    </section>
  </main>
</body>
</html>
```